Design a website for a newly developed Delta 8 THC Company

Design a responsive Website with the following goals in mind:
- Built on Wordpress/WooCommerce theme. Please use this when designing for ease of integration.
- Build trust with website visitors with an engaging, informative content driven website, that leads to a conversion of product purchase and repeat business. We will also be driving consumers to businesses that carry our products as well.
- The website will embody a lifestyle feel and make the visitor identify with the content.
- The website will allow for super charged SEO and other digital marketing and advertising strategies and tactics used to increase discovery, awareness, and conversion.
Please see additional goals in the uploaded files.
Target Market(s)
Male/Female 21-
Industry/Entity Type
Cannabis/Hemp
Coding
Coded - Design and coding required
Number of Pages Required
5+ page
Font styles to use
Other font styles liked:
- Montserrat
Look and feel
Each slider illustrates characteristics of the customer's brand and the style your logo design should communicate.

```html
<!DOCTYPE html>
<html lang="en">
<head>
<meta charset="utf-8">
<title>Auralis — Delta 8</title>
<link href="https://fonts.googleapis.com/css2?family=Montserrat:wght@400;500;600;700&family=Open+Sans:wght@400;600&display=swap" rel="stylesheet">
<style>
:root{
  --gold:#c9963a;
  --gold-light:#d9a84a;
  --yellow:#e8c64a;
  --brown:#5a2e1a;
  --ink:#222222;
  --text:#444444;
  --hero-bg:#e9e9e9;
  --light:#f7f7f7;
  --footer:#0b0b0b;
  --white:#ffffff;
}
*{box-sizing:border-box;margin:0;padding:0}
html,body{width:1200px;height:3888px;overflow:hidden}
body{position:relative;font-family:"Open Sans",Arial,sans-serif;color:var(--text);background:var(--white)}
.abs{position:absolute}
.mont{font-family:"Montserrat",Arial,sans-serif}

/* header */
.topbar{left:0;top:0;width:1200px;height:59px;background:var(--white)}
.topbar .title{left:358px;top:20px;font:700 17px "Montserrat",sans-serif;color:var(--ink)}
.topbar .tag{left:573px;top:22px;font-size:13px;color:var(--text)}
.navbar{left:0;top:59px;width:1200px;height:102px;background:var(--gold)}
.nav-item{top:41px;font:500 15px "Montserrat",sans-serif;color:var(--white)}
.nav-item.active{text-decoration:underline;text-underline-offset:4px}
.nav-icon{top:38px}
.brand-badge{left:112px;top:5px;width:202px;height:202px;border-radius:50%;background:#111;box-shadow:0 4px 12px rgba(0,0,0,.35);display:flex;align-items:center;justify-content:center;font:600 24px "Montserrat",sans-serif;color:var(--gold);letter-spacing:4px}

/* hero */
.hero{left:0;top:161px;width:1200px;height:594px;background:var(--hero-bg)}
.hero h1{left:89px;top:148px;width:560px;font:700 45px/1.23 "Montserrat",sans-serif;color:var(--ink)}
.hero .lead{left:89px;top:353px;font:600 15px "Open Sans",sans-serif;color:var(--ink)}
.btn-gold{left:89px;top:397px;width:137px;height:47px;background:var(--gold);color:var(--white);font:600 17px "Montserrat",sans-serif;display:flex;align-items:center;justify-content:center;border-radius:3px;box-shadow:0 3px 6px rgba(0,0,0,.2)}
.hero-photo{left:596px;top:35px;width:513px;height:536px;border-radius:8px;background:radial-gradient(circle at 55% 45%,#4fa63a 0%,#2f7d23 45%,#1f5a18 70%,rgba(233,233,233,0) 72%)}
.round-arrow{width:44px;height:44px;border-radius:50%;background:var(--yellow);display:flex;align-items:center;justify-content:center}

/* sections */
.section-title{left:0;width:1200px;text-align:center;font:700 39px "Montserrat",sans-serif;color:var(--brown)}
.section-sub{left:0;width:1200px;text-align:center;font-size:15px;line-height:30px;color:var(--text)}

.cat-card{top:958px;width:235px;height:310px;background:var(--white);box-shadow:0 0 8px rgba(0,0,0,.18)}
.cat-photo{position:absolute;left:12px;top:30px;width:211px;height:250px}
.cat-name{top:1289px;width:235px;text-align:center;font:600 17px "Montserrat",sans-serif;color:var(--ink)}
.cat-price{top:1313px;width:235px;text-align:center;font:600 17px "Montserrat",sans-serif;color:var(--gold-light)}

.about{left:0;top:1400px;width:1200px;height:622px;background:linear-gradient(135deg,#c48f33 0%,#d4a24a 50%,#c28c30 100%)}
.about-mark{left:136px;top:86px;width:400px;height:400px;border-radius:50%;background:#141414;display:flex;align-items:center;justify-content:center;font:600 46px "Montserrat",sans-serif;letter-spacing:8px;color:var(--gold)}
.about h2{left:599px;top:112px;font:700 38px "Montserrat",sans-serif;color:var(--white)}
.about p{left:599px;top:177px;width:490px;font-size:15px;line-height:30px;color:var(--white)}
.btn-outline{left:599px;top:482px;width:138px;height:45px;border:2px solid var(--white);color:var(--white);font:600 17px "Montserrat",sans-serif;display:flex;align-items:center;justify-content:center;border-radius:3px}

.testi{top:2241px;width:242px;height:243px;background:var(--white);box-shadow:0 0 8px rgba(0,0,0,.14);overflow:hidden}
.testi.faded{opacity:.55}
.testi .avatar{position:absolute;left:14px;top:14px;width:52px;height:52px;border-radius:50%;background:linear-gradient(#8a9aa6,#4b5964)}
.testi .name{position:absolute;left:76px;top:28px;font:600 17px "Montserrat",sans-serif;color:var(--gold)}
.testi .quote{position:absolute;left:14px;top:76px;width:220px;font-size:13px;line-height:30px;color:var(--ink)}
.testi .stars{position:absolute;left:14px;top:200px;color:var(--gold-light);font-size:14px;letter-spacing:3px}
.dot{top:2521px;width:11px;height:11px;border-radius:50%;background:#cfcfcf}

.gallery{left:0;top:2618px;width:1200px;height:863px;background:var(--light)}
.tile{position:absolute}

/* footer */
.footer{left:0;top:3481px;width:1200px;height:407px;background:var(--footer);color:var(--white)}
.footer .brand{left:90px;top:110px;width:270px;text-align:center;font:600 26px "Montserrat",sans-serif;letter-spacing:5px;color:var(--gold)}
.footer .desc{left:90px;top:200px;font-size:13px;line-height:30px}
.card-badge{top:288px;width:50px;height:30px;border-radius:3px;background:var(--white)}
.footer h4{top:62px;font:700 16px "Montserrat",sans-serif;text-decoration:underline;text-underline-offset:6px}
.footer ul{list-style:none;font-size:15px;line-height:30px}
.footer li::before{content:"»";margin-right:16px}
.contact-row{font-size:15px;line-height:30px;display:flex;gap:18px}
.contact-row svg{flex:none;margin-top:8px}
.social{top:3764px;width:16px;height:16px;border-radius:50%;background:var(--white)}
.footer .rule{left:90px;top:325px;width:1060px;height:1px;background:#777}
.footer .copy{left:0;top:357px;width:1200px;text-align:center;font-size:14px}
</style>
</head>
<body>

<header>
  <div class="abs topbar">
    <div class="abs title">LOREM IPSUM DOLOR</div>
    <div class="abs tag">Lorem ipsum dolor sit amet, consectetur adipiscing elit</div>
  </div>
  <nav class="abs navbar">
    <span class="abs nav-item active" style="left:407px">HOME</span>
    <span class="abs nav-item" style="left:480px">ABOUT US</span>
    <span class="abs nav-item" style="left:583px">PRODUCTS</span>
    <span class="abs nav-item" style="left:691px">REVIEWS</span>
    <span class="abs nav-item" style="left:788px">BLOGS</span>
    <span class="abs nav-item" style="left:866px">CONTACT US</span>
    <svg class="abs nav-icon" style="left:998px" width="12" height="16" viewBox="0 0 12 16"><circle cx="6" cy="4" r="3.5" fill="#fff"/><path d="M0 15c0-5 2.5-7 6-7s6 2 6 7z" fill="#fff"/></svg>
    <svg class="abs nav-icon" style="left:1034px" width="15" height="16" viewBox="0 0 15 16"><circle cx="6" cy="6" r="4.5" fill="none" stroke="#fff" stroke-width="2.2"/><path d="M9.5 9.5l4 4.5" stroke="#fff" stroke-width="2.5"/></svg>
    <svg class="abs nav-icon" style="left:1071px" width="15" height="16" viewBox="0 0 15 16"><path d="M0 2h3l2 8h8l2-6H4" fill="none" stroke="#fff" stroke-width="2"/><circle cx="6" cy="13.5" r="1.6" fill="#fff"/><circle cx="12" cy="13.5" r="1.6" fill="#fff"/></svg>
  </nav>
  <div class="abs brand-badge">AURALIS</div>
</header>

<section class="abs hero">
  <h1 class="abs">Lorem ipsum dolor sit amet, consectetur a dipiscing elit</h1>
  <p class="abs lead">Lorem ipsum dolor sit amet, consectetur adipiscing.</p>
  <a class="abs btn-gold">Shop Now</a>
  <div class="abs hero-photo" role="img" aria-label="Green pouch of Delta 8 gummies with colourful jar lids"></div>
  <div class="abs round-arrow" style="left:17px;top:271px"><svg width="10" height="14" viewBox="0 0 10 14"><path d="M7 2L2 7l5 5" fill="none" stroke="#222" stroke-width="2"/></svg></div>
  <div class="abs round-arrow" style="left:1125px;top:271px"><svg width="10" height="14" viewBox="0 0 10 14"><path d="M3 2l5 5-5 5" fill="none" stroke="#222" stroke-width="2"/></svg></div>
</section>

<section>
  <h2 class="abs section-title" style="top:828px">Our Product Categories</h2>
  <p class="abs section-sub" style="top:874px">Lorem ipsum dolor sit amet, consectetur adipiscing elit, sed do eiusmod tempor<br>incididunt ut labore et dolore magna aliqua.</p>
  <svg class="abs" style="left:40px;top:1105px" width="20" height="54" viewBox="0 0 20 54"><path d="M17 2L3 27l14 25" fill="none" stroke="#222" stroke-width="2"/></svg>
  <svg class="abs" style="left:1138px;top:1105px" width="20" height="54" viewBox="0 0 20 54"><path d="M3 2l14 25L3 52" fill="none" stroke="#222" stroke-width="2"/></svg>

  <div class="abs cat-card" style="left:94px"><div class="cat-photo" role="img" aria-label="Green pouch of gummies" style="background:linear-gradient(160deg,#4da23a,#23611b)"></div></div>
  <div class="abs cat-card" style="left:353px"><div class="cat-photo" role="img" aria-label="Vape device with hemp flower buds" style="background:radial-gradient(ellipse at center,#6e6e6e 0%,#9b8a66 35%,#fff 70%)"></div></div>
  <div class="abs cat-card" style="left:611px"><div class="cat-photo" role="img" aria-label="Green pouch of gummies" style="background:linear-gradient(160deg,#4da23a,#23611b)"></div></div>
  <div class="abs cat-card" style="left:871px"><div class="cat-photo" role="img" aria-label="Vape pen with cartridges" style="background:radial-gradient(ellipse at center,#c7b07a 0%,#efe7d4 40%,#fff 70%)"></div></div>

  <div class="abs cat-name" style="left:94px">Product Name</div><div class="abs cat-price" style="left:94px">$84.99</div>
  <div class="abs cat-name" style="left:353px">Product Name</div><div class="abs cat-price" style="left:353px">$84.99</div>
  <div class="abs cat-name" style="left:611px">Product Name</div><div class="abs cat-price" style="left:611px">$84.99</div>
  <div class="abs cat-name" style="left:871px">Product Name</div><div class="abs cat-price" style="left:871px">$84.99</div>
</section>

<section class="abs about">
  <div class="abs about-mark">AURALIS</div>
  <h2 class="abs">ABOUT DELTA 8</h2>
  <p class="abs">Lorem ipsum dolor sit amet, consectetur adipiscing elit, sed do eius-mod tempor incididunt ut labore et dolore magna aliqua. Ut enim ad minim veniam, quis nostrud exercitation ullamco laboris nisi ut aliquip ex ea commodo consequat. Duis aute irure dolor in reprehenderit in voluptate velit esse cillum dolore eu fugiat nulla pariatur. Excepteur sint occaecat cupidatat non proident, sunt in culpa qui officia deserunt mollit anim id est laborum.Sed ut perspiciatis unde omnis iste natus error sit voluptatem accusantium doloremque laudantium, totam rem aperiam.i</p>
  <a class="abs btn-outline">Learn More</a>
</section>

<section>
  <h2 class="abs section-title" style="top:2100px">Our Client Testimonials</h2>
  <p class="abs section-sub" style="top:2146px">Lorem ipsum dolor sit amet, consectetur adipiscing elit, sed do eiusmod tempor<br>incididunt ut labore et dolore magna aliqua.</p>

  <div class="abs testi faded" style="left:-44px"><div class="avatar"></div><div class="name">John Deo</div><p class="quote">Lorem ipsum dolor sit amet, conse ctetur adipiscing elit, sed do eius mod tempor incididunt ut labore et dolore magna aliqua.</p><div class="stars">★★★★★</div></div>
  <div class="abs testi" style="left:217px"><div class="avatar"></div><div class="name">John Deo</div><p class="quote">Lorem ipsum dolor sit amet, conse ctetur adipiscing elit, sed do eius mod tempor incididunt ut labore et dolore magna aliqua.</p><div class="stars">★★★★★</div></div>
  <div class="abs testi" style="left:480px;box-shadow:0 6px 16px rgba(0,0,0,.2)"><div class="avatar"></div><div class="name">John Deo</div><p class="quote">Lorem ipsum dolor sit amet, conse ctetur adipiscing elit, sed do eius mod tempor incididunt ut labore et dolore magna aliqua.</p><div class="stars">★★★★★</div></div>
  <div class="abs testi" style="left:741px"><div class="avatar"></div><div class="name">John Deo</div><p class="quote">Lorem ipsum dolor sit amet, conse ctetur adipiscing elit, sed do eius mod tempor incididunt ut labore et dolore magna aliqua.</p><div class="stars">★★★★★</div></div>
  <div class="abs testi faded" style="left:1002px"><div class="avatar"></div><div class="name">John Deo</div><p class="quote">Lorem ipsum dolor sit amet, conse ctetur adipiscing elit, sed do eius mod tempor incididunt ut labore et dolore magna aliqua.</p><div class="stars">★★★★★</div></div>

  <span class="abs dot" style="left:573px;background:var(--gold)"></span>
  <span class="abs dot" style="left:587px"></span>
  <span class="abs dot" style="left:601px"></span>
  <span class="abs dot" style="left:615px"></span>
</section>

<section class="abs gallery">
  <h2 class="abs section-title" style="top:78px">Our Gallery</h2>
  <p class="abs section-sub" style="top:124px">Lorem ipsum dolor sit amet, consectetur adipiscing elit, sed do eiusmod tempor<br>incididunt ut labore et dolore magna aliqua.</p>
  <div class="tile" role="img" aria-label="Amber gummy bears on a dark surface" style="left:116px;top:207px;width:317px;height:330px;background:linear-gradient(160deg,#1b1410,#7a3a14 55%,#2a1c14)"></div>
  <div class="tile" role="img" aria-label="Gummy bears beside a hemp leaf on pink" style="left:442px;top:207px;width:317px;height:228px;background:linear-gradient(120deg,#f3c6d6,#8ab04a 45%,#f1d27a 70%,#f3c6d6)"></div>
  <div class="tile" role="img" aria-label="Pile of colourful gummy candies" style="left:767px;top:207px;width:316px;height:330px;background:linear-gradient(135deg,#e94b4b,#f0a23a 35%,#5bb34a 60%,#d94d8f)"></div>
  <div class="tile" role="img" aria-label="Hand holding sugared gummies among leaves" style="left:442px;top:444px;width:317px;height:332px;background:linear-gradient(180deg,#2e4a22,#6c7d3e 45%,#e2b9a0 75%,#caa18c)"></div>
  <div class="tile" role="img" aria-label="Bowl of bright gummy bears" style="left:116px;top:546px;width:317px;height:230px;background:linear-gradient(150deg,#3a6fa8,#f2b632 40%,#d9402e 70%,#f4f0ea)"></div>
  <div class="tile" role="img" aria-label="Cola-shaped gummies in a dark bowl" style="left:767px;top:546px;width:316px;height:230px;background:linear-gradient(150deg,#2a1a16,#6a2a1e 50%,#141010)"></div>
</section>

<footer class="abs footer">
  <div class="abs brand">AURALIS</div>
  <p class="abs desc">Lorem ipsum dolor sit amet, consectetur<br>adipiscing elit, sed do eiusmod.</p>
  <span class="abs card-badge" style="left:90px"></span>
  <span class="abs card-badge" style="left:146px"></span>
  <span class="abs card-badge" style="left:202px"></span>
  <span class="abs card-badge" style="left:258px"></span>

  <h4 class="abs" style="left:415px">QIUCK LINKS</h4>
  <ul class="abs" style="left:415px;top:103px">
    <li>Home</li><li>About us</li><li>Categories</li><li>Reviews</li><li>Contact Us</li>
  </ul>

  <h4 class="abs" style="left:662px">IMPORTANT</h4>
  <ul class="abs" style="left:662px;top:103px">
    <li>Privacy Policy</li><li>Shipping Policy</li><li>Refund Policy</li><li>Terms &amp; Conditions</li>
  </ul>

  <h4 class="abs" style="left:895px">CONTACT INFO</h4>
  <div class="abs contact-row" style="left:897px;top:103px">
    <svg width="12" height="16" viewBox="0 0 12 16"><path d="M6 0a6 6 0 0 0-6 6c0 4.5 6 10 6 10s6-5.5 6-10a6 6 0 0 0-6-6z" fill="#fff"/><circle cx="6" cy="6" r="2.2" fill="#0b0b0b"/></svg>
    <span>123 Lorem ipsum dolor sit amet,<br>consectetur adipiscing</span>
  </div>
  <div class="abs contact-row" style="left:897px;top:172px">
    <svg width="14" height="14" viewBox="0 0 14 14"><path d="M3 0l3 3-2 2c1 2 3 4 5 5l2-2 3 3-2 3C6 14 0 8 0 3z" fill="#fff"/></svg>
    <span>+ 123 456 7890</span>
  </div>
  <div class="abs contact-row" style="left:895px;top:215px">
    <svg width="16" height="12" viewBox="0 0 16 12"><rect width="16" height="12" fill="#fff"/><path d="M0 0l8 7 8-7" fill="none" stroke="#0b0b0b" stroke-width="1.5"/></svg>
    <span>hello@auralishemp.com</span>
  </div>
  <div class="abs rule"></div>
  <p class="abs copy">© Copyrights 2020 &nbsp;Delta 8 &nbsp;| &nbsp;&nbsp;All Rights Reserved</p>
</footer>
<span class="abs social" style="left:902px"></span>
<span class="abs social" style="left:924px"></span>
<span class="abs social" style="left:952px"></span>
<span class="abs social" style="left:981px"></span>

</body>
</html>
```